SKYWARD LENSWORKS New Wordpress Design Project

Skyward Lensworks is a photo-sharing site for aviation photographers and enthusiasts.

Please redesign the home page (http://www.skywardlensworks.example/) and photo feature page (http://www.skywardlensworks.example/2014/10/borvel-freight-23/).

We like and would like to keep the logo we have, but are open to changing colors on the logo to suit a new color scheme if necessary.
Updates

Hi All, Thank you for taking part in this design competition. Could you please show us your first round design concepts within 24hrs as we hope to show our client them and start providing feedback? Much appreciated, Lex VH BramblePeak Design

Hi All, A few tips: Could you try keep the search bar above the fold Include a section for showing new blog posts Try to integrate an ads a little better also above and below the fold Appreciated, Lex Vh

Target Market(s)

Aviation photographers and enthusiasts of all age groups globally.

Industry/Entity Type

Aviation

Requirements
Must have
• • Clean and consistent layout
• A good way to incorporate advertisements on the home page and photo feature page
• Clear and simple menu navigation
• On home page – call to action to register
• On home page - call to action to upload photos
• On home page – social buttons call to action to follow, circle, like, etc
• On photo feature page – call to action to tweet, +1, Like, etc a photo
Nice to have
• Sites we like

www.quillpane.example
http://www.layoutorchard.example/demo/45176.html
Should not have
• • Unnecessary animations
• No Adobe Flash
• Overly crowded / busy design

```html
<!DOCTYPE html>
<html lang="en">
<head>
<meta charset="utf-8">
<title>Skyward Lensworks</title>
<link rel="stylesheet" href="https://fonts.googleapis.com/css2?family=Ubuntu:wght@400;500;700&family=Noto+Sans:wght@400;700&display=swap">
<style>
:root{
  --orange:#f39a12;
  --orange-dark:#d27a05;
  --orange-light:#ffb640;
  --ink:#1b1b1b;
  --grey-text:#9a9a9a;
  --sky-top:#1d3f93;
  --sky-mid:#3a6cc4;
  --ground:#a67d44;
  --cream:#fdf6e6;
  --mist:#e9e9e7;
  --footer:#a8814b;
  --footer-dark:#7d5f37;
  --white:#ffffff;
  --tile-edge:#e7900f;
}
*{box-sizing:border-box;margin:0;padding:0}
html,body{width:1200px;height:3000px;overflow:hidden}
body{position:relative;background:var(--white);font-family:"Noto Sans",Verdana,sans-serif;color:var(--ink)}
.abs{position:absolute}
.heading{font-family:"Ubuntu",sans-serif;font-weight:500;font-size:38px;letter-spacing:1px;text-align:center;width:1200px;left:0;color:var(--ink)}
.heading .accent{color:var(--orange)}
.lede{left:190px;width:820px;text-align:center;font-size:15px;line-height:25px;color:var(--grey-text)}

/* hero */
.hero{left:0;top:0;width:1200px;height:700px;background:linear-gradient(180deg,var(--sky-top) 0%,var(--sky-mid) 45%,#6f8fb8 62%,#b68f54 70%,var(--ground) 85%,#c9a775 100%)}
.hero-fade{left:0;top:660px;width:1200px;height:60px;background:linear-gradient(180deg,rgba(255,255,255,0),#fff)}
.brand{left:134px;top:30px;display:flex;align-items:center;gap:10px;font-family:"Ubuntu",sans-serif;font-weight:700;font-size:34px;color:#111}
.brand-dot{width:20px;height:20px;border-radius:50%;background:var(--orange)}
.search{left:610px;top:24px;width:246px;height:24px;border:1px solid rgba(255,255,255,.35);background:rgba(20,50,120,.5);color:#9fb3d8;font-size:12px;padding:3px 8px}
.account{left:910px;top:24px;display:flex}
.account span{display:block;height:26px;line-height:26px;padding:0 16px;font-size:13px;color:#fff;background:linear-gradient(180deg,var(--orange-light),var(--orange-dark))}
.account span:first-child{border-radius:13px 0 0 13px;border-right:1px solid #b86a04}
.account span:last-child{border-radius:0 13px 13px 0}
.menu{left:580px;top:66px;display:flex;gap:34px;font-size:17px;color:#fff}
.menu .current{color:var(--orange);border-bottom:3px solid var(--orange);padding-bottom:4px}
.hero-plane{left:20px;top:100px;width:1160px;height:400px;background:radial-gradient(ellipse at 50% 60%,rgba(240,240,245,.35),rgba(255,255,255,0) 60%)}
.hero-text{left:200px;top:508px;width:800px;text-align:center;color:#fff;font-size:17px;line-height:26px;text-shadow:0 1px 2px rgba(0,0,0,.4)}
.read-more{left:532px;top:624px;width:134px;height:36px;border:2px solid #fff;border-radius:3px;color:#fff;font-size:19px;line-height:32px;text-align:center}
.dots{left:934px;top:638px;display:flex;gap:14px}
.dots i{display:block;width:18px;height:18px;border-radius:50%;background:#fff}
.dots i.on{background:var(--orange);border:2px solid #fff}

/* gallery */
.tile{border:2px solid var(--tile-edge);overflow:hidden;background:#111}
.tile .photo{width:100%;height:calc(100% - 46px)}
.tile .caption{height:46px;line-height:44px;text-align:center;color:#eee;font-family:"Ubuntu",sans-serif;font-size:20px;background:#111}
.btn-orange{background:linear-gradient(180deg,var(--orange-light),var(--orange) 55%,var(--orange-dark));color:#fff;font-family:"Ubuntu",sans-serif;text-align:center;box-shadow:0 4px 6px rgba(0,0,0,.25)}
.more-gallery{left:450px;top:1320px;width:300px;height:64px;line-height:64px;font-size:25px}

/* talent */
.talent-bg{left:0;top:1430px;width:1200px;height:420px;background:linear-gradient(180deg,#fff 0%,#f1f1f0 40%,#e4e4e2 100%)}
.upload{left:270px;top:1702px;width:260px;height:78px;font-size:38px;line-height:78px;display:flex;align-items:center;justify-content:center;gap:30px}
.login-account{left:590px;top:1702px;width:340px;height:78px;font-size:38px;line-height:78px}

/* categories */
.category-band{left:0;top:1850px;width:1200px;height:412px;background:var(--cream)}
.tabs{left:130px;top:1980px;width:940px;height:52px;background:linear-gradient(180deg,#4a4a4a,#0d0d0d);display:flex;padding-left:140px;font-family:"Ubuntu",sans-serif;font-size:20px;color:#aaa}
.tabs span{padding:0 28px;line-height:52px}
.tabs .active{color:var(--orange);background:#000;position:relative}
.tabs .active::after{content:"";position:absolute;left:50%;bottom:-14px;margin-left:-12px;border:12px solid transparent;border-top-color:var(--orange);border-bottom:0}
.thumb{top:2064px;height:126px;border:2px solid #e6cfa3}
.arrow{top:2116px;width:24px;height:24px}

/* testimonial */
.voice-band{left:0;top:2262px;width:1200px;height:380px;background:linear-gradient(180deg,#ececec,#dedede)}
.avatar{left:564px;top:2364px;width:72px;height:72px;border-radius:50%;border:3px solid var(--orange);background:radial-gradient(circle at 50% 40%,#f2c89d,#d99a57)}
.quote-mark{font-family:"Ubuntu",sans-serif;font-size:140px;color:#c9c9c9;line-height:1}

/* footer */
.footer{left:0;top:2642px;width:1200px;height:288px;background:linear-gradient(180deg,#b08a55,var(--footer) 50%,#9b763f)}
.footer-bottom{left:0;top:2930px;width:1200px;height:70px;background:var(--footer-dark);color:#fff;font-size:15px;line-height:70px;text-align:center}
.col-title{font-family:"Ubuntu",sans-serif;font-weight:700;font-size:20px;color:#fff;letter-spacing:1px}
.footer-text{font-size:15px;line-height:24px;color:#fff}
.email-field{left:196px;top:2808px;width:280px;height:38px;border:2px solid #d7bd92;background:rgba(120,90,50,.35);color:#e3d2b3;font-size:15px;line-height:34px;padding-left:10px}
.submit{left:198px;top:2866px;width:82px;height:32px;line-height:32px;font-size:15px}
.quick-links{left:566px;top:2732px;list-style:none;font-size:15px;color:#fff}
.quick-links li{height:37px}
.social{width:38px;height:38px;border-radius:5px;background:#f4e7d1}
</style>
</head>
<body>

<!-- hero -->
<div class="abs hero"></div>
<div class="abs hero-plane" role="img" aria-label="Airliner approaching head-on over the runway against a blue sky"></div>
<div class="abs hero-fade"></div>
<div class="abs brand"><span class="brand-dot"></span>Skyward Lensworks</div>
<div class="abs search">Search</div>
<div class="abs account"><span>Login</span><span>Register</span></div>
<nav class="abs menu"><span class="current">Home</span><span>Gallery</span><span>Submit a photo</span><span>Airport search</span></nav>
<p class="abs hero-text">Lorem Ipsum is simply dummy text of the printing and typesetting industry. Lorem Ipsum has been the industry's standard dummy text ever since the 1500s, when an unknown printer took a galley of type and scrambled it to make a type specimen book. It has survived not only five centuries,</p>
<div class="abs read-more">Read More</div>
<div class="abs dots"><i class="on"></i><i></i><i></i><i></i></div>

<!-- gallery -->
<h2 class="abs heading" style="top:742px"><span class="accent">Skyward</span> Lensworks Gallery</h2>
<p class="abs lede" style="top:812px">Lorem Ipsum is simply dummy text of the printing and typesetting industry. Lorem Ipsum has been the industry's standard dummy text ever since the 1500s, when an unknown printer took a galley of type and scrambled it to make a type specimen book. It has survived not only five cen-</p>

<div class="abs tile" style="left:130px;top:926px;width:300px;height:236px">
  <div class="photo" role="img" aria-label="Jet climbing through white clouds" style="background:linear-gradient(180deg,#4f86c9,#a9c7e6 60%,#2c3a2a)"></div>
  <div class="caption">Neque porro quisquam</div>
</div>
<div class="abs tile" style="left:130px;top:1180px;width:300px;height:238px">
  <div class="photo" role="img" aria-label="Business jet over a deep blue sea" style="background:linear-gradient(160deg,#1c3f78,#0d2450)"></div>
  <div class="caption">Neque porro quisquam</div>
</div>
<div class="abs tile" style="left:450px;top:926px;width:300px;height:350px">
  <div class="photo" role="img" aria-label="Airliner banking overhead in a clear blue sky" style="background:linear-gradient(180deg,#0e3d8e,#3d7fd0 70%,#1a2a20)"></div>
  <div class="caption">Neque porro quisquam</div>
</div>
<div class="abs btn-orange more-gallery">More Photo Gallery</div>
<div class="abs tile" style="left:770px;top:926px;width:300px;height:236px">
  <div class="photo" role="img" aria-label="Airliner above clouds at golden sunset" style="background:linear-gradient(180deg,#c98a3a,#f3c06a 40%,#5a4330)"></div>
  <div class="caption">Neque porro quisquam</div>
</div>
<div class="abs tile" style="left:770px;top:1180px;width:300px;height:238px">
  <div class="photo" role="img" aria-label="Airliner taking off from a runway at dusk" style="background:linear-gradient(180deg,#7d8fa6,#e7b977 55%,#6b7a3c)"></div>
  <div class="caption">Neque porro quisquam</div>
</div>

<!-- talent -->
<div class="abs talent-bg" role="img" aria-label="Faded runway stretching to the horizon"></div>
<h2 class="abs heading" style="top:1522px">Display &nbsp;Your <span class="accent">Photography</span> Tallent Here</h2>
<p class="abs lede" style="top:1590px">Lorem Ipsum is simply dummy text of the printing and typesetting industry. Lorem Ipsum has been the industry's standard dummy text ever since the 1500s, when an unknown printer took a galley of type and scrambled it to make a type specimen book. It has survived not only five cen-</p>
<div class="abs btn-orange upload">
  <svg width="46" height="46" viewBox="0 0 46 46" aria-hidden="true"><circle cx="23" cy="23" r="20" fill="none" stroke="#3a2a10" stroke-width="3"/><path d="M23 33V14M14 22l9-9 9 9" fill="none" stroke="#3a2a10" stroke-width="5" stroke-linecap="round" stroke-linejoin="round"/></svg>
  <span>Upload</span>
</div>
<div class="abs btn-orange login-account">Login Account</div>

<!-- categories -->
<div class="abs category-band"></div>
<h2 class="abs heading" style="top:1890px">Get <span class="accent">Photographs</span> By Category</h2>
<div class="abs tabs"><span class="active">Airport</span><span>Photographer</span><span>Photo Size</span><span>Upload Date</span></div>
<svg class="abs arrow" style="left:128px" viewBox="0 0 24 24" aria-hidden="true"><rect x="1" y="1" width="22" height="22" fill="none" stroke="#e6cfa3" stroke-width="2"/><path d="M15 6l-6 6 6 6" fill="none" stroke="#e6cfa3" stroke-width="2"/></svg>
<div class="abs thumb" role="img" aria-label="Jet climbing through clouds" style="left:190px;width:160px;background:linear-gradient(180deg,#4f86c9,#c7dbef)"></div>
<div class="abs thumb" role="img" aria-label="Airliner on the runway at sunset" style="left:370px;width:218px;background:linear-gradient(180deg,#8da0b5,#f0c27c 55%,#7a8b45)"></div>
<div class="abs thumb" role="img" aria-label="Airliner banking in a blue sky" style="left:612px;width:216px;background:linear-gradient(180deg,#0e3d8e,#4f8ad6)"></div>
<div class="abs thumb" role="img" aria-label="Business jet over the sea" style="left:852px;width:156px;background:linear-gradient(160deg,#1c3f78,#0d2450)"></div>
<svg class="abs arrow" style="left:1046px" viewBox="0 0 24 24" aria-hidden="true"><rect x="1" y="1" width="22" height="22" fill="none" stroke="#e6cfa3" stroke-width="2"/><path d="M9 6l6 6-6 6" fill="none" stroke="#e6cfa3" stroke-width="2"/></svg>

<!-- testimonial -->
<div class="abs voice-band" role="img" aria-label="Faint business jet in the background"></div>
<h2 class="abs heading" style="top:2306px">Our <span class="accent">Photographers</span> Says</h2>
<div class="abs avatar" role="img" aria-label="Photographer portrait"></div>
<div class="abs quote-mark" style="left:148px;top:2440px">“</div>
<p class="abs lede" style="top:2474px">Lorem Ipsum is simply dummy text of the printing and typesetting industry. Lorem Ipsum has been the industry's standard dummy text ever since the 1500s, when an unknown printer took a galley of type and scrambled it to make a type specimen book. It has survived not only five cen-</p>
<div class="abs quote-mark" style="left:1018px;top:2500px">”</div>

<!-- footer -->
<div class="abs footer"></div>
<div class="abs col-title" style="left:194px;top:2694px">News Letter</div>
<p class="abs footer-text" style="left:196px;top:2726px;width:290px">when an unknown printer took a galley of type and scrambled it</p>
<div class="abs email-field">Your E-mail</div>
<div class="abs btn-orange submit">Submit</div>

<div class="abs col-title" style="left:562px;top:2694px">Quick Links</div>
<ul class="abs quick-links"><li>Home</li><li>Gallery</li><li>Submit a photo</li><li>Airport search</li><li>contact Us</li></ul>

<div class="abs col-title" style="left:804px;top:2694px">Follow Us On</div>
<div class="abs social" style="left:806px;top:2732px" role="img" aria-label="Social link"></div>
<div class="abs social" style="left:858px;top:2732px" role="img" aria-label="Social link"></div>
<div class="abs social" style="left:910px;top:2732px" role="img" aria-label="Social link"></div>
<div class="abs social" style="left:964px;top:2732px" role="img" aria-label="Social link"></div>
<div class="abs social" style="left:806px;top:2794px" role="img" aria-label="Social link"></div>
<div class="abs social" style="left:858px;top:2794px" role="img" aria-label="Social link"></div>
<div class="abs social" style="left:910px;top:2794px" role="img" aria-label="Social link"></div>
<div class="abs social" style="left:964px;top:2794px" role="img" aria-label="Social link"></div>

<div class="abs footer-bottom">All Rights Reserved@ 2014 hello@skywardlensworks.example</div>

</body>
</html>
```